Soccer Club Site Redesign

We are a suburban youth soccer club in need of a web site redesign. Our current site’s look/feel is outdated and is in need of a more modern look. What we are looking for is a design layout that will accommodate the current functionality we have for the site and give us an updated modern look. The deliverable for this project will be .psd file that can be converted to an html theme file for Wordpress. We will take care of the conversion and handle the html coding/javascript functionality.
Take a look at our current site to get an idea of what we offer and the current layout we have.
http://www.fernwickfootball.org
Our club hosts youth recreational soccer, traveling soccer and two large soccer tournaments during the year. We also sponsor a number of training clinics. Our site serves a couple primary purposes:
1. Parents learn how/where/when to sign up their child for the leagues we offer.
2. Parents learn dates/times of various events the club offers.
3. Other soccer clubs get information on the tournaments we offer, sign up for the tournaments etc.
We do a pretty good job of presenting information about the various events/leagues available and how to sign up for them, but we want to do a better job of presenting a calendar where parents can quickly find dates/times of various events. Ideally, we would like to incorporate a news section (like we currently have), with a calendar and the use of more images on the home page. We understand screen space is limited but would incorporate jquery/javascript widgets to hide/show info and maybe an ‘imagebox’ for the additional images.
Here are a few sites with ideas that we liked:
http://sports.dorrington.edu/ (Look at the Upcoming Events calendar on the page)
http://www.ashvalekickers.com/ (look at the Upcoming Events calendar in the right column and the image box in the main content area)
http://www.plumetfutbol.com/index.php (Like the look and use of images)
http://www.rqkickersclub.com/ (imagebox use)
http://www.lorvanpuckclub.org/ ( hockey website but like the use of crisp header graphics)
http://www.ellisfordpuck.com/ (another hockey site, like the calendar used)
That should give you a pretty good idea of what we are looking for. The new design will need to accommodate the existing functionality of the site. Our logo (which is attached) should be incorporated into the site….otherwise we are open to your design ideas.

```html
<!DOCTYPE html>
<html lang="en">
<head>
<meta charset="utf-8">
<title>Fernwick Soccer Club</title>
<link href="https://fonts.googleapis.com/css2?family=PT+Sans+Narrow:wght@700&family=Ubuntu:ital,wght@0,400;0,500;0,700;1,400&display=swap" rel="stylesheet">
<style>
:root{
  --royal:#1433b8;
  --royal-deep:#0a1f8f;
  --navy:#0d1f5e;
  --ink:#13237a;
  --orange:#f0760e;
  --amber:#f2a20c;
  --btn:#f7a10a;
  --paper:#ffffff;
  --mist:#f3f3f3;
  --line:#d8d8d8;
  --footer:#e6e6e6;
  --base:#2e2e2e;
  --text:#333;
}
*{margin:0;padding:0;box-sizing:border-box}
html,body{width:702px;height:1200px;overflow:hidden}
body{position:relative;background:var(--footer);font-family:"Ubuntu",sans-serif;color:var(--ink)}
.abs{position:absolute}

.header-band{left:0;top:0;width:702px;height:370px;background:radial-gradient(ellipse at 50% 40%,#2a5ae8 0%,var(--royal) 45%,var(--royal-deep) 100%)}
.main-nav{left:28px;top:58px;width:647px;height:35px;background:var(--navy);border:1px solid #5b78e0;border-radius:3px 3px 0 0}
.main-nav a{position:absolute;top:12px;color:#fff;font-size:8.5px;font-weight:500;text-decoration:none;letter-spacing:.1px}
.club-mark{left:330px;top:10px;width:40px;height:40px;border-radius:50%;background:var(--navy);border:2px solid #fff}
.club-name{left:310px;top:71px;width:80px;text-align:center;color:#fff;font-size:9px;font-weight:700;letter-spacing:.6px}

.hero{left:28px;top:94px;width:647px;height:256px;border:2px solid #fff;background:#fff}
.hero-photo{left:0;top:0;width:449px;height:252px;background:linear-gradient(120deg,#2d4f9e 0%,#5d78b8 30%,#c9272f 55%,#e8e0dc 70%,#3a56a8 100%)}
.hero-copy{left:470px;top:116px;width:200px}
.hero-title{font-family:"PT Sans Narrow",sans-serif;font-weight:700;font-size:20px;color:var(--navy);line-height:1.1}
.hero-lead{font-family:"PT Sans Narrow",sans-serif;font-weight:700;font-size:11px;color:var(--navy);line-height:1.25;margin-top:7px}
.hero-copy p{font-size:7.4px;line-height:1.55;color:var(--ink);margin-top:7px}
.hero-btn{top:278px;height:19px;width:70px;background:var(--btn);color:#fff;font-size:8.5px;font-weight:700;text-align:center;line-height:19px}
.dots{left:503px;top:316px;display:flex;gap:4px}
.dots span{width:8px;height:8px;background:#a9b7e0}
.dots span:first-child{background:var(--royal-deep)}

.content{left:27px;top:370px;width:648px;height:668px;background:var(--paper)}
.welcome{left:43px;top:388px;width:408px}
.section-title{font-size:11px;font-weight:500;color:var(--navy);letter-spacing:.1px}
.welcome h1{font-size:12px;font-weight:500;color:var(--navy)}
.welcome p{font-size:7.2px;line-height:1.7;margin-top:5px;color:var(--ink)}

.events{left:41px;width:410px}
.day-head{height:20px;background:var(--navy);color:#fff;font-size:7.5px;line-height:20px;padding-left:12px}
.col-head{display:flex;gap:2px;height:17px;margin-top:2px}
.col-head span{flex:1;color:#fff;font-size:7.5px;line-height:17px;padding-left:14px;background:var(--amber)}
.col-head span:first-child{background:var(--orange)}
.rows{background:var(--mist);padding:8px 0 6px}
.row{display:flex;height:21.5px;align-items:center;font-size:7.5px;color:var(--ink)}
.row .c1{width:132px;padding-left:15px}
.row .c2{width:142px}
.row .c3{width:42px}

.news{left:464px;top:378px;width:202px;height:458px;border:1px solid var(--line);background:#fff}
.news .section-title{position:absolute;left:11px;top:11px}
.news-item{position:absolute;left:0;width:200px;height:82px;border-bottom:1px solid var(--line)}
.date{position:absolute;left:11px;top:10px;width:40px;height:41px;background:var(--royal);color:#fff;text-align:center;font-size:10px;line-height:1.3;padding-top:4px}
.date b{display:block;font-weight:400;border-bottom:1px solid #6d86e0;padding-bottom:1px;margin-bottom:1px}
.news-body{position:absolute;left:60px;top:10px;width:136px;font-size:6.6px;line-height:1.6;color:var(--text)}
.news-body h3{font-size:7.6px;font-weight:700;color:var(--navy);line-height:1.4;margin-bottom:1px}
.news-body em{font-style:normal;font-weight:700}

.clubs{left:45px;top:853px}
.tile{top:876px;width:145px}
.tile-img{width:145px;height:66px}
.tile h4{font-size:7.8px;font-weight:700;color:var(--navy);line-height:1.45;margin:11px 2px 0}
.tile p{font-size:7.8px;line-height:1.45;color:var(--royal);margin:6px 2px 0}

.footer-col{top:1056px;font-size:7.6px;line-height:16px;color:var(--text)}
.footer-rule{top:1056px;width:1px;height:94px;background:#b8b8b8}
.connect{left:392px;top:1057px;font-size:8.4px;font-style:italic;color:var(--text)}
.social{left:393px;top:1075px;display:flex;gap:7px}
.social span{width:18px;height:18px;border-radius:50%}
.social-names{left:393px;top:1107px;font-size:7.6px;font-style:italic;color:var(--text)}
.base-bar{left:0;top:1173px;width:702px;height:27px;background:var(--base);color:#bdbdbd;font-size:6.4px;line-height:27px;padding-left:42px}
</style>
</head>
<body>

<div class="abs header-band"></div>

<nav class="abs main-nav">
  <a style="left:20px">HOME</a>
  <a style="left:61px">ABOUT US</a>
  <a style="left:115px">CALENDAR</a>
  <a style="left:173px">RECREATIONAL</a>
  <a style="left:246px">FORMS</a>
  <a style="left:365px">TOURNAMENTS</a>
  <a style="left:440px">COACHES</a>
  <a style="left:493px">VOLUNTEERS</a>
  <a style="left:559px">CONTACT US</a>
</nav>
<div class="abs club-mark"></div>
<div class="abs club-name">FERNWICK</div>

<section class="abs hero">
  <div class="abs hero-photo" role="img" aria-label="Photo of a youth soccer player in a red and white striped kit dribbling past defenders in blue"></div>
</section>
<div class="abs hero-copy">
  <div class="hero-title">World best soccer club</div>
  <div class="hero-lead">Duis quam. Nam eget lacus. Aliquam erat volutpat. Quisque dignissim leo.</div>
  <p>Proin dui lectus, cursus eu, mattis laoreet, viverra sit amet, quam.</p>
  <p>Curabitur vel dolor ultrices ipsum dictum tristique. Praesent vitae lacus. Ut velit enim, vestibulum non, fermentum nec, hendrerit quis, leo. Pellentesque rutrum malesuada neque.</p>
</div>
<div class="abs hero-btn" style="left:498px">VIEW MORE</div>
<div class="abs hero-btn" style="left:573px">LEARN MORE</div>
<div class="abs dots"><span></span><span></span><span></span><span></span></div>

<div class="abs content"></div>

<section class="abs welcome">
  <h1>WELCOME TO THE FERNWICK SOCCER CLUB!</h1>
  <p>Phasellus felis dolor, scelerisque a, tempus eget, lobortis id, libero. Donec scelerisque leo ac risus. Praesent sit amet est. In dictum, dolor eu dictum porttitor, enim felis viverra mi, eget luctus massa purus quis odio.</p>
  <p>Etiam nulla massa, pharetra facilisis, volutpat in, imperdiet sit amet, sem. Aliquam nec erat at purus cursus interdum. Vestibulum ligula augue, bibendum accumsan, vestibulum ut, commodo a, mi. Morbi ornare gravida elit. Integer congue, augue et malesuada iaculis, ipsum dui aliquet felis, at cursus magna nisl nec elit. Donec iaculis diam a nisi accumsan viverra. Duis sed tellus et tortor vestibulum gravida. Praesent elementum elit at tellus. Curabitur metus ipsum, luctus eu, malesuada ut, tincidunt sed, diam.</p>
</section>

<div class="abs section-title" style="left:41px;top:526px">UPCOMING EVENT</div>

<section class="abs events" style="top:545px">
  <div class="day-head">Monday, November 13</div>
  <div class="col-head"><span>Tournament Name</span><span>Event Name</span><span>Timing - Location</span></div>
  <div class="rows">
    <div class="row"><span class="c1">Final Soccer Tournamnet</span><span class="c2">at Halden - River Bend</span><span class="c3">6.00 pm</span><span>River Bend, HD</span></div>
    <div class="row"><span class="c1">SECOND SEMIS Women</span><span class="c2">at Halden - River Bend</span><span class="c3">6.00 pm</span><span>River Bend, HD</span></div>
  </div>
</section>
<section class="abs events" style="top:642px">
  <div class="day-head">Friday, November 18</div>
  <div class="col-head"><span>Tournament Name</span><span>Event Name</span><span>Timing - Location</span></div>
  <div class="rows">
    <div class="row"><span class="c1">Final Soccer Tournamnet</span><span class="c2">at Halden - River Bend</span><span class="c3">6.00 pm</span><span>River Bend, HD</span></div>
    <div class="row"><span class="c1">SECOND SEMIS Women</span><span class="c2">at Halden - River Bend</span><span class="c3">6.00 pm</span><span>River Bend, HD</span></div>
  </div>
</section>
<section class="abs events" style="top:736px">
  <div class="day-head">Sunday, November 25</div>
  <div class="col-head"><span>Tournament Name</span><span>Event Name</span><span>Timing - Location</span></div>
  <div class="rows">
    <div class="row"><span class="c1">Final Soccer Tournamnet</span><span class="c2">at Halden - River Bend</span><span class="c3">6.00 pm</span><span>River Bend, HD</span></div>
    <div class="row"><span class="c1">SECOND SEMIS Women</span><span class="c2">at Halden - River Bend</span><span class="c3">6.00 pm</span><span>River Bend, HD</span></div>
  </div>
</section>

<aside class="abs news">
  <div class="section-title">UPCOMING NEWS</div>
  <div class="news-item" style="top:34px">
    <div class="date"><b>OCT</b>28</div>
    <div class="news-body"><h3>Mandatory D10 meeting for the B1 Bantams and B1 Peewees</h3>Proin nulla arcu, nonummy luctus,<br>8:00am - 10:00 am<br><em>Tag(s):</em> Competitive&nbsp; Recreational</div>
  </div>
  <div class="news-item" style="top:116px">
    <div class="date"><b>OCT</b>23</div>
    <div class="news-body"><h3>Mauris vel lacus vitae felis vestibulum volutpat.</h3>Proin nulla arcu, nonummy luctus,<br>8:00am - 10:00 am<br><em>Tag(s):</em> Competitive&nbsp; Recreational</div>
  </div>
  <div class="news-item" style="top:198px">
    <div class="date"><b>OCT</b>20</div>
    <div class="news-body"><h3>Class aptent taciti sociosqu ad litora torquent per conubia nostra</h3>Proin nulla arcu, nonummy luctus,<br>8:00am - 10:00 am<br><em>Tag(s):</em> Competitive&nbsp; Recreational</div>
  </div>
  <div class="news-item" style="top:280px">
    <div class="date"><b>OCT</b>06</div>
    <div class="news-body"><h3>Duis sed tellus et tortor vestibulum gravida.</h3>Proin nulla arcu, nonummy luctus,<br>8:00am - 10:00 am<br><em>Tag(s):</em> Competitive&nbsp; Recreational</div>
  </div>
  <div class="news-item" style="top:362px;border-bottom:0">
    <div class="date"><b>AUG</b>20</div>
    <div class="news-body"><h3>Fusce id felis. Vivamus sollicitudin metus eget eros.</h3>Proin nulla arcu, nonummy luctus,<br>8:00am - 10:00 am<br><em>Tag(s):</em> Competitive&nbsp; Recreational</div>
  </div>
</aside>

<div class="abs section-title clubs">ABOUT BEST TOURNAMENTS &amp; CLUBS</div>

<article class="abs tile" style="left:44px">
  <div class="tile-img" role="img" aria-label="Photo of players' boots around a ball on green turf" style="background:linear-gradient(180deg,#b8492c,#4f7a2e)"></div>
  <h4>Proin dui lectus, cursus eu, mattis laoreet, viverra sit amet, quam.</h4>
  <p>Curabitur vel dolor ultrices ipsum dictum tristique. Praesent vitae lacus. Ut velit enim, vestibulum non,</p>
</article>
<article class="abs tile" style="left:202px">
  <div class="tile-img" role="img" aria-label="Photo of two women's teams contesting the ball on a pitch" style="background:linear-gradient(180deg,#8fa3b8,#3d6b2d)"></div>
  <h4>Proin dui lectus, cursus eu, mattis laoreet, viverra sit amet, quam.</h4>
  <p>Curabitur vel dolor ultrices ipsum dictum tristique. Praesent vitae lacus. Ut velit enim, vestibulum non,</p>
</article>
<article class="abs tile" style="left:361px">
  <div class="tile-img" role="img" aria-label="Photo of a team in blue kits running during a match" style="background:linear-gradient(180deg,#3a5aa8,#6a86b8)"></div>
  <h4>Proin dui lectus, cursus eu, mattis laoreet, viverra sit amet, quam.</h4>
  <p>Curabitur vel dolor ultrices ipsum dictum tristique. Praesent vitae lacus. Ut velit enim, vestibulum non,</p>
</article>
<article class="abs tile" style="left:520px;top:874px">
  <div class="tile-img" role="img" aria-label="Photo of players in red and light blue chasing the ball" style="background:linear-gradient(180deg,#c0403a,#5b8a3a)"></div>
  <h4>Proin dui lectus, cursus eu, mattis laoreet, viverra sit amet, quam.</h4>
  <p>Curabitur vel dolor ultrices ipsum dictum tristique. Praesent vitae lacus. Ut velit enim, vestibulum non,</p>
</article>

<footer>
  <div class="abs footer-col" style="left:45px">Home<br>About Us<br>Calendar<br>Recreational<br>Forms<br>Tournaments</div>
  <div class="abs footer-rule" style="left:115px"></div>
  <div class="abs footer-col" style="left:137px">Volunteers<br>Contact Us<br>Sponsors<br>Refers<br>Maps<br>Links</div>
  <div class="abs footer-rule" style="left:199px"></div>
  <div class="abs footer-col" style="left:220px;top:1057px">References<br>Support<br>News<br>Blog<br>Coaches</div>
  <div class="abs footer-rule" style="left:277px"></div>
  <div class="abs footer-col" style="left:301px;top:1057px">Volunteers<br>Contact Us<br>Sponsors<br>Refers<br>Maps</div>
  <div class="abs footer-rule" style="left:365px"></div>
  <div class="abs connect">Get Connected</div>
  <div class="abs social"><span style="background:#3b4f8f"></span><span style="background:#3a9ed8"></span><span style="background:#b0b0b0"></span><span style="background:#9a9a9a"></span><span style="background:#f07a1a"></span></div>
  <div class="abs social-names">Circlepage &nbsp;| Chirpline | Vidstream | Rss | <span style="font-style:normal">Worknet</span></div>
  <div class="abs base-bar">© 2012 Company Name.&nbsp; All right reserved.&nbsp; Term of use</div>
</footer>

</body>
</html>
```